Technology Company Web Design Project

We are working with BrimLoop. They are a technology company and in need of a new website design.
BrimLoop helps companies control who (or what) can access which information inside their systems — and under what conditions. Think of them as the traffic controller for digital access and data permissions.
Instead of letting every app, employee, or AI bot freely connect to everything, GateMarrow makes sure:
• Each one only gets access to what it actually needs.
• That access follows company rules automatically.
• Those rules are enforced the same way everywhere — across apps, servers, and even AI tools.
Some competitor sites to use for inspiration:
https://www.korvanshield.com/en/lp/ac/korvanmesh.html
https://www.dunmerecharter.org
https://www.qelvo.com
Thank you for taking the time to consider designing a website for us. We are web developers based in Stockton and Los Angeles, CA, USA. Most of our projects go through the same process. Understanding this process may help you win a project with us. We custom-code all of our websites in-house. We don’t have any requirements as to what tools you use for your design, but we prefer Figma files. For any design that we label as four-stars, we send it to the client for review. The client picks the final design they want us to use. Once we complete this process, we will continue to show additional clients all the four-star sites and purchase them later. Your designs will have multiple chances to sell. For better chances of success, we ask that you follow these guidelines.
IMAGES:
If you use any images or icons in the design, we ask that you have a link to the asset so we can purchase the image/icon. Most of the designs we submit do not have the customer’s images on them unless they have some great images. Be creative; show us the feeling you are trying to portray with your image choices. Use any royalty-free site you choose. We subscribe to Tarsel and mainly use their images, but we can purchase images outside of Tarsel.
PLEASE NOTE: we will not submit designs to clients with watermarks on the images.
FONTS:
We ask that you identify the fonts used in the design. This can be done in a message if you want. We typically use Google Fonts and Tarsel Fonts.
CONTENT:
We're always open to different content and ideas. We often submit designs with stock images so the client can see our vision. We typically take pictures after the website launch to use their images with our vision. Lorem Ipsum is fine for paragraphs, but we ask that you write the headers in correct English. We want to be able to show the vision and identify the sections of the website.
INSPIRATION:
We typically add a couple of links in the brief of websites we like to help you get started in your design.
REVISIONS:
We do not often ask for revisions of the designs unless we see something in the design that may not appeal to the client. If there are slight changes that we want to make, we do that in the development process.
FEEDBACK:
We rarely give feedback on designs during the design process. We are working on many website projects and do not have the time to provide feedback. We usually respond if your request is well thought out and asks specific questions, but a note asking “feedback, please” usually goes unanswered.

```html
<!DOCTYPE html>
<html lang="en">
<head>
<meta charset="utf-8">
<title>BrimLoop — The Traffic Controller for Your Digital Access</title>
<link href="https://fonts.googleapis.com/css2?family=Poppins:wght@400;500;600;700&display=swap" rel="stylesheet">
<style>
:root{
  --navy:#1d3a5c;
  --navy-deep:#152c47;
  --orange:#e9812f;
  --orange-deep:#d9722a;
  --ink:#1b1b1b;
  --muted:#5d6470;
  --panel:#ececec;
  --soft:#f1f5f9;
  --white:#ffffff;
}
*{box-sizing:border-box;margin:0;padding:0}
html,body{width:1200px;height:4040px;overflow:hidden}
body{font-family:"Poppins",sans-serif;color:var(--ink);background:var(--white);position:relative}
.abs{position:absolute}
a{color:inherit;text-decoration:none}

/* header */
.site-header{position:absolute;top:0;left:0;width:1200px;height:90px;background:var(--white);z-index:3}
.brand{position:absolute;left:62px;top:24px;display:flex;align-items:center;gap:10px;font-weight:700;font-size:26px;letter-spacing:1px;color:var(--navy)}
.brand-dot{width:30px;height:30px;border-radius:50%;background:var(--navy)}
.main-nav{position:absolute;top:36px;left:0;font-size:15px;color:var(--ink)}
.main-nav a{position:absolute;white-space:nowrap}
.main-nav a.active{color:var(--orange)}
.main-nav a.active::after{content:"";position:absolute;left:50%;top:28px;width:6px;height:6px;margin-left:-3px;border-radius:50%;background:var(--orange)}
.btn{display:inline-flex;align-items:center;justify-content:center;border-radius:30px;font-weight:500;font-size:14px;letter-spacing:.5px;text-transform:uppercase}
.btn-orange{background:var(--orange);color:var(--white)}
.btn-ghost{border:1.5px solid var(--white);color:var(--white)}
.btn-white{background:var(--white);color:var(--orange)}

/* hero */
.hero{position:absolute;top:90px;left:0;width:1200px;height:640px}
.hero-title{position:absolute;left:62px;top:100px;font-size:47px;line-height:56px;font-weight:600;color:var(--white);text-transform:uppercase;letter-spacing:.5px}
.hero-title em{font-style:normal;color:var(--orange)}
.hero-lead{position:absolute;left:62px;top:285px;width:520px;font-size:16px;line-height:25px;color:var(--white)}
.hero-actions{position:absolute;left:60px;top:365px;display:flex;gap:28px}
.hero-actions .btn{height:40px;padding:0 24px}
.hero-art{position:absolute;left:680px;top:60px;width:500px;height:380px;border-radius:50%;background:radial-gradient(circle at 45% 50%,#4fb7e8 0%,#2a6f9f 35%,rgba(29,58,92,0) 70%)}

/* welcome */
.welcome-art{position:absolute;left:110px;top:683px;width:478px;height:415px;border-radius:24px;background:linear-gradient(160deg,#fdf3e6 0%,#f7d9b0 55%,#eceff3 100%)}
.welcome-copy{position:absolute;left:653px;top:748px;width:445px}
.section-title{font-size:35px;font-weight:600;text-transform:uppercase;color:var(--ink);letter-spacing:.5px}
.welcome-copy p{font-size:12.5px;line-height:19.5px;color:var(--muted);margin-top:12px}
.welcome-copy p:first-of-type{margin-top:20px}
.welcome-copy .btn{margin-top:24px;height:40px;width:150px}

/* services */
.services{position:absolute;top:1169px;left:0;width:1200px;height:832px;background:var(--panel)}
.centered{position:absolute;left:0;width:1200px;text-align:center}
.service-card{position:absolute;width:348px;height:292px;background:var(--white);border-radius:14px;overflow:hidden}
.service-card .blob{position:absolute;left:0;top:0}
.service-card .icon{position:absolute;left:22px;top:20px}
.service-card h3{position:absolute;left:75px;top:115px;width:240px;font-size:16.5px;line-height:24px;font-weight:600;color:var(--ink)}
.service-card p{position:absolute;left:75px;top:172px;width:240px;font-size:12.5px;line-height:19.5px;color:var(--muted)}
.service-card .more{position:absolute;left:75px;top:240px;font-size:13px;font-weight:500;color:var(--orange);text-decoration:underline}

/* how it works */
.subtitle{font-size:13px;line-height:20px;color:var(--muted)}
.step{position:absolute;top:2198px;width:289px;height:259px;border-radius:8px;background:var(--soft);text-align:center}
.step .badge{position:absolute;left:103px;top:40px;width:82px;height:82px;border-radius:50%;background:var(--navy);display:flex;align-items:center;justify-content:center}
.step h3{position:absolute;left:0;width:100%;top:143px;font-size:17px;font-weight:600;color:var(--ink)}
.step p{position:absolute;left:20px;width:249px;top:180px;font-size:12.5px;line-height:20px;color:var(--muted)}
.step.featured{background:var(--orange)}
.step.featured h3,.step.featured p{color:var(--white)}
.step.featured .badge{background:var(--white)}

/* resources */
.resources{position:absolute;top:2531px;left:0;width:1200px;height:646px;background:var(--panel)}
.post{position:absolute;top:2732px;width:257px;height:370px;background:var(--white);border-radius:14px;overflow:hidden}
.post svg{position:absolute;left:7px}
.post h3{position:absolute;left:20px;width:215px;font-size:16px;line-height:24px;font-weight:600;color:var(--navy)}
.post p{position:absolute;left:20px;width:215px;font-size:12px;line-height:19.5px;color:var(--muted)}

/* contact */
.contact{position:absolute;top:3177px;left:0;width:1200px;height:863px;background:var(--orange-deep)}
.contact .section-title,.contact .subtitle{color:var(--white)}
.field{position:absolute;height:44px;border:1.5px solid rgba(255,255,255,.85);border-radius:24px;display:flex;align-items:center;padding-left:20px;font-size:12.5px;color:var(--white)}
.field .sep{width:1px;height:22px;background:rgba(255,255,255,.7);margin:0 14px}
.field.filled{background:var(--white);color:var(--ink)}
.field.filled .sep{background:#c9c9c9}
.field.message{align-items:flex-start;padding-top:12px;border-radius:26px}

/* footer */
.footer-brand{position:absolute;left:0;width:1200px;top:3830px;display:flex;justify-content:center;align-items:center;gap:12px;font-size:32px;font-weight:600;letter-spacing:2px;color:var(--white)}
.footer-brand .brand-dot{background:var(--white);width:34px;height:34px}
.rule{position:absolute;left:60px;width:1080px;height:1px;background:rgba(255,255,255,.3)}
.contact-item{position:absolute;top:3938px;display:flex;align-items:center;gap:14px;font-size:14px;color:var(--white)}
.contact-item .dot{width:38px;height:38px;border-radius:50%;background:var(--orange);display:flex;align-items:center;justify-content:center;box-shadow:0 0 0 3px rgba(233,129,47,.35)}
.copyright{position:absolute;left:0;width:1200px;top:4008px;text-align:center;font-size:12px;color:var(--white)}
</style>
</head>
<body>

<header class="site-header">
  <a class="brand" href="#"><span class="brand-dot"></span>BRIMLOOP</a>
  <nav class="main-nav">
    <a class="active" href="#" style="left:381px">Home</a>
    <a href="#" style="left:458px">About US</a>
    <a href="#" style="left:560px">Services</a>
    <a href="#" style="left:654px">How It Works</a>
    <a href="#" style="left:783px">Resources</a>
    <a href="#" style="left:893px">Contact</a>
  </nav>
  <a class="btn btn-orange abs" href="#" style="left:990px;top:25px;width:150px;height:42px">Get Started</a>
</header>

<section class="hero">
  <svg class="abs" style="left:0;top:0" width="1200" height="640" viewBox="0 0 1200 640">
    <path d="M0,0 H1200 V375 C1120,450 1000,515 820,522 C620,530 440,500 290,522 C160,542 70,585 0,620 Z" fill="var(--navy)"/>
  </svg>
  <div class="hero-art" role="img" aria-label="Glowing digital hand touching a holographic access interface"></div>
  <h1 class="hero-title">The <em>Traffic</em><br><em>Controller</em> for<br>your digital access</h1>
  <p class="hero-lead">BrimLoop enforces secure, consistent, and automated access control across your apps, servers, and AI tools.</p>
  <div class="hero-actions">
    <a class="btn btn-orange" href="#">Get Started</a>
    <a class="btn btn-ghost" href="#">How It Works</a>
  </div>
</section>

<section class="welcome">
  <div class="welcome-art" role="img" aria-label="Illustration of a person working at a desk with security alert icons around"></div>
  <div class="welcome-copy">
    <h2 class="section-title">Welcome BrimLoop</h2>
    <p>Lorem Ipsum has been the industry's standard dummy text ever since the 1500s, when an unknown printer took a galley of type and scrambled it to make a type specimen book. It has survived not only five centuries, but also the leap into electronic typesetting, remaining essentially unchanged.</p>
    <p>Lorem Ipsum has been the industry's standard dummy text ever since the 1500s, when an unknown printer took a galley of type and scrambled it to make a type specimen book. It has survived not only five centuries, but also the leap into electronic typesetting, remaining essentially unchanged.</p>
    <a class="btn btn-orange" href="#">View More</a>
  </div>
</section>

<section class="services">
  <h2 class="section-title centered" style="top:72px">Our Services</h2>
</section>

<!-- service cards -->
<article class="service-card" style="left:60px;top:1321px">
  <svg class="blob" width="200" height="165" viewBox="0 0 200 165"><path d="M0,0 H195 C172,62 125,92 72,100 C36,106 12,122 0,160 Z" fill="var(--navy)"/></svg>
  <svg class="icon" width="58" height="58" viewBox="0 0 58 58" fill="none" stroke="#fff" stroke-width="2"><rect x="6" y="10" width="30" height="24" rx="2"/><path d="M12 18h18M12 24h12"/><rect x="30" y="30" width="20" height="16" rx="2"/><path d="M34 30v-5a6 6 0 0 1 12 0v5"/></svg>
  <h3>Access Control Management</h3>
  <p>Lorem Ipsum has been the industry's standard dummy text ever since the 1500s.</p>
  <a class="more" href="#">View More</a>
</article>
<article class="service-card" style="left:425px;top:1321px">
  <svg class="blob" width="200" height="165" viewBox="0 0 200 165"><path d="M0,0 H195 C172,62 125,92 72,100 C36,106 12,122 0,160 Z" fill="var(--orange)"/></svg>
  <svg class="icon" width="58" height="58" viewBox="0 0 58 58" fill="none" stroke="#fff" stroke-width="2"><rect x="8" y="6" width="30" height="36" rx="2"/><path d="M14 14h18M14 20h18M14 26h10"/><path d="M42 28l10 4v8c0 6-5 10-10 12-5-2-10-6-10-12v-8z"/></svg>
  <h3>Identity &amp; Policy Enforcement</h3>
  <p>Lorem Ipsum has been the industry's standard dummy text ever since the 1500s.</p>
  <a class="more" href="#">View More</a>
</article>
<article class="service-card" style="left:791px;top:1321px">
  <svg class="blob" width="200" height="165" viewBox="0 0 200 165"><path d="M0,0 H195 C172,62 125,92 72,100 C36,106 12,122 0,160 Z" fill="var(--navy)"/></svg>
  <svg class="icon" width="58" height="58" viewBox="0 0 58 58" fill="none" stroke="#fff" stroke-width="2"><rect x="10" y="14" width="24" height="20" rx="3"/><circle cx="18" cy="24" r="2"/><circle cx="26" cy="24" r="2"/><path d="M22 14V8M6 40h30"/><rect x="34" y="34" width="16" height="14" rx="2"/><path d="M37 34v-4a5 5 0 0 1 10 0v4"/></svg>
  <h3>Ai &amp; Automation Access Governance</h3>
  <p>Lorem Ipsum has been the industry's standard dummy text ever since the 1500s.</p>
  <a class="more" href="#">View More</a>
</article>
<article class="service-card" style="left:60px;top:1630px">
  <svg class="blob" width="200" height="165" viewBox="0 0 200 165"><path d="M0,0 H195 C172,62 125,92 72,100 C36,106 12,122 0,160 Z" fill="var(--navy)"/></svg>
  <svg class="icon" width="58" height="58" viewBox="0 0 58 58" fill="none" stroke="#fff" stroke-width="2"><circle cx="29" cy="22" r="14"/><circle cx="29" cy="20" r="5"/><path d="M20 32c3-5 15-5 18 0M10 44h10M38 44h10M29 36v12"/></svg>
  <h3>Integration &amp; Deployment Services</h3>
  <p>Lorem Ipsum has been the industry's standard dummy text ever since the 1500s.</p>
  <a class="more" href="#">View More</a>
</article>
<article class="service-card" style="left:425px;top:1630px">
  <svg class="blob" width="200" height="165" viewBox="0 0 200 165"><path d="M0,0 H195 C172,62 125,92 72,100 C36,106 12,122 0,160 Z" fill="var(--navy)"/></svg>
  <svg class="icon" width="58" height="58" viewBox="0 0 58 58" fill="none" stroke="#fff" stroke-width="2"><rect x="6" y="8" width="44" height="30" rx="2"/><circle cx="30" cy="22" r="8"/><path d="M36 28l6 6M20 46h18M28 38v8"/></svg>
  <h3>Monitoring &amp; Continuous Improvement</h3>
  <p>Lorem Ipsum has been the industry's standard dummy text ever since the 1500s.</p>
  <a class="more" href="#">View More</a>
</article>
<article class="service-card" style="left:791px;top:1630px">
  <svg class="blob" width="200" height="165" viewBox="0 0 200 165"><path d="M0,0 H195 C172,62 125,92 72,100 C36,106 12,122 0,160 Z" fill="var(--navy)"/></svg>
  <svg class="icon" width="58" height="58" viewBox="0 0 58 58" fill="none" stroke="#fff" stroke-width="2"><rect x="10" y="8" width="30" height="40" rx="2"/><path d="M18 8v-3h14v3M16 20h18M16 27h18M16 34h10"/><circle cx="40" cy="42" r="8"/><path d="M36 42l3 3 5-5"/></svg>
  <h3>Compliance &amp; Audit Support</h3>
  <p>Lorem Ipsum has been the industry's standard dummy text ever since the 1500s.</p>
  <a class="more" href="#">View More</a>
</article>

<section class="how">
  <h2 class="section-title centered" style="top:2070px">How It Works</h2>
  <p class="subtitle centered" style="top:2128px;left:400px;width:400px">Lorem Ipsum has been the industry's standard dummy text ever since the 1500s.</p>
  <div class="step" style="left:146px">
    <div class="badge"><svg width="44" height="44" viewBox="0 0 44 44" fill="none" stroke="#fff" stroke-width="2"><rect x="16" y="10" width="12" height="10" rx="2"/><path d="M18 10V7a4 4 0 0 1 8 0v3M22 20v6M8 26h28M10 26v8M34 26v8M22 26v10"/></svg></div>
    <h3>Precise Access Control</h3>
    <p>Each user, app, or bot gets access only to what's necessary.</p>
  </div>
  <div class="step featured" style="left:455px">
    <div class="badge"><svg width="44" height="44" viewBox="0 0 44 44" fill="none" stroke="var(--orange)" stroke-width="2"><rect x="8" y="6" width="22" height="28" rx="2"/><path d="M13 13h12M13 19h12M13 25h7"/><circle cx="31" cy="31" r="8"/><path d="M27 31l3 3 5-5"/></svg></div>
    <h3>Consistent Enforcement</h3>
    <p>Policies apply everywhere — across servers, APIs, and AI integrations.</p>
  </div>
  <div class="step" style="left:764px">
    <div class="badge"><svg width="44" height="44" viewBox="0 0 44 44" fill="none" stroke="#fff" stroke-width="2"><rect x="10" y="6" width="24" height="32" rx="2"/><rect x="15" y="16" width="14" height="10" rx="3"/><circle cx="19" cy="21" r="1.5"/><circle cx="25" cy="21" r="1.5"/><path d="M22 16v-4M16 32h12"/></svg></div>
    <h3>Policy Automation</h3>
    <p>Build once, enforce automatically at scale.</p>
  </div>
</section>

<section class="resources">
  <h2 class="section-title centered" style="top:75px">Resources</h2>
  <p class="subtitle centered" style="top:129px;left:370px;width:460px">Lorem Ipsum has been the industry's standard dummy text ever since the 1500s, when an unknown printer took a galley.</p>
</section>

<defs></defs>
<article class="post" style="left:60px">
  <svg style="top:7px" width="243" height="160" viewBox="0 0 243 160" role="img" aria-label="Photo of a team working together in a bright office">
    <defs><linearGradient id="gOffice" x1="0" y1="0" x2="1" y2="1"><stop offset="0" stop-color="#c9ccc6"/><stop offset="1" stop-color="#5c6158"/></linearGradient></defs>
    <path d="M10,0 H233 Q243,0 243,10 V110 C180,150 80,120 0,160 V10 Q0,0 10,0 Z" fill="url(#gOffice)"/>
  </svg>
  <h3 style="top:195px">Lorem Ipsum Has Been The Industry's</h3>
  <p style="top:255px">Lorem Ipsum has been the industry's standard dummy text ever since the 1500s, when an unknown printer took a galley of type and scrambled.</p>
</article>
<article class="post" style="left:334px">
  <h3 style="top:15px">Lorem Ipsum Has Been The Industry's</h3>
  <p style="top:75px">Lorem Ipsum has been the industry's standard dummy text ever since the 1500s, when an unknown printer took a galley of type and scrambled.</p>
  <svg style="top:200px" width="243" height="163" viewBox="0 0 243 163" role="img" aria-label="Photo of a control room with screens at night">
    <defs><linearGradient id="gControl" x1="0" y1="0" x2="0" y2="1"><stop offset="0" stop-color="#233a5a"/><stop offset="1" stop-color="#0d1726"/></linearGradient></defs>
    <path d="M0,40 C80,5 170,30 243,0 V153 Q243,163 233,163 H10 Q0,163 0,153 Z" fill="url(#gControl)"/>
  </svg>
</article>
<article class="post" style="left:609px">
  <svg style="top:7px" width="243" height="160" viewBox="0 0 243 160" role="img" aria-label="Photo of hands on a laptop with a digital security shield overlay">
    <defs><linearGradient id="gLaptop" x1="0" y1="0" x2="1" y2="1"><stop offset="0" stop-color="#2b6f8f"/><stop offset="1" stop-color="#182838"/></linearGradient></defs>
    <path d="M10,0 H233 Q243,0 243,10 V110 C180,150 80,120 0,160 V10 Q0,0 10,0 Z" fill="url(#gLaptop)"/>
  </svg>
  <h3 style="top:195px">Lorem Ipsum Has Been The Industry's</h3>
  <p style="top:255px">Lorem Ipsum has been the industry's standard dummy text ever since the 1500s, when an unknown printer took a galley of type and scrambled.</p>
</article>
<article class="post" style="left:882px">
  <h3 style="top:15px">Lorem Ipsum Has Been The Industry's</h3>
  <p style="top:75px">Lorem Ipsum has been the industry's standard dummy text ever since the 1500s, when an unknown printer took a galley of type and scrambled.</p>
  <svg style="top:200px" width="243" height="163" viewBox="0 0 243 163" role="img" aria-label="Image of a human hand and robotic hand reaching toward a digital lock">
    <defs><linearGradient id="gHands" x1="0" y1="0" x2="1" y2="1"><stop offset="0" stop-color="#1f5a7a"/><stop offset="1" stop-color="#0b1a2b"/></linearGradient></defs>
    <path d="M0,40 C80,5 170,30 243,0 V153 Q243,163 233,163 H10 Q0,163 0,153 Z" fill="url(#gHands)"/>
  </svg>
</article>

<section class="contact">
  <h2 class="section-title centered" style="top:75px">Contact Us</h2>
  <p class="subtitle centered" style="top:129px;left:370px;width:460px">Lorem Ipsum has been the industry's standard dummy text ever since the 1500s, when an unknown printer took a galley.</p>
  <svg class="abs" style="left:0;top:413px" width="1200" height="450" viewBox="0 0 1200 450">
    <path d="M0,240 C200,190 400,172 600,184 C850,196 1050,140 1200,20 V450 H0 Z" fill="var(--navy)"/>
  </svg>
</section>

<form class="contact-form">
  <div class="field filled" style="left:275px;top:3372px;width:318px">
    <svg width="14" height="14" viewBox="0 0 14 14" fill="var(--navy)"><circle cx="7" cy="4" r="3.2"/><path d="M1 14c0-4 3-6 6-6s6 2 6 6z"/></svg><span class="sep"></span>First Name*</div>
  <div class="field" style="left:604px;top:3372px;width:322px">
    <svg width="14" height="14" viewBox="0 0 14 14" fill="#fff"><circle cx="7" cy="4" r="3.2"/><path d="M1 14c0-4 3-6 6-6s6 2 6 6z"/></svg><span class="sep"></span>Last Name*</div>
  <div class="field" style="left:275px;top:3431px;width:318px">
    <svg width="15" height="12" viewBox="0 0 15 12" fill="#fff"><path d="M0 1h15v10H0z"/><path d="M0 1l7.5 6L15 1" stroke="var(--orange-deep)" fill="none" stroke-width="1.4"/></svg><span class="sep"></span>Email*</div>
  <div class="field" style="left:604px;top:3431px;width:322px">
    <svg width="14" height="14" viewBox="0 0 14 14" fill="#fff"><path d="M3 0l3 3-2 2c1 2 3 4 5 5l2-2 3 3-2 3C6 14 0 8 0 2z"/></svg><span class="sep"></span>Phone No*</div>
  <div class="field message" style="left:275px;top:3491px;width:651px;height:74px">
    <svg width="16" height="14" viewBox="0 0 16 14" fill="#fff" style="margin-top:2px"><path d="M0 1h11v7H4l-3 3V8H0z"/><path d="M12 4h4v7h-1v3l-3-3H6V9h6z"/></svg><span class="sep" style="margin-top:-2px"></span>Messages*</div>
  <a class="btn btn-white abs" href="#" style="left:525px;top:3601px;width:150px;height:38px">View More</a>
</form>

<footer class="site-footer">
  <div class="footer-brand"><span class="brand-dot"></span>BRIMLOOP</div>
  <div class="rule" style="top:3919px"></div>
  <div class="contact-item" style="left:268px">
    <span class="dot"><svg width="16" height="16" viewBox="0 0 14 14" fill="#fff"><path d="M3 0l3 3-2 2c1 2 3 4 5 5l2-2 3 3-2 3C6 14 0 8 0 2z"/></svg></span>+ 0100 555 014</div>
  <div class="contact-item" style="left:514px">
    <span class="dot"><svg width="16" height="12" viewBox="0 0 15 12" fill="#fff"><path d="M0 1h15v10H0z"/><path d="M0 1l7.5 6L15 1" stroke="var(--orange)" fill="none" stroke-width="1.4"/></svg></span>info@brimloop.com</div>
  <div class="contact-item" style="left:769px">
    <span class="dot"><svg width="14" height="18" viewBox="0 0 14 18" fill="#fff"><path d="M7 0a7 7 0 0 1 7 7c0 5-7 11-7 11S0 12 0 7a7 7 0 0 1 7-7z"/><circle cx="7" cy="7" r="2.5" fill="var(--orange)"/></svg></span>brimloop company...</div>
  <div class="rule" style="top:3993px"></div>
  <p class="copyright">© Copyright 2025 brimloop.All Rights Reserved</p>
</footer>

</body>
</html>
```